Guarenteed! - Homepage Website Design - Coding not required- Winner to complete further pages

Hi all,

We're looking at redesigning our current website with a few adjustments to other pages but the main adjustments will be on the homepage which is what this design request is for. Please note : any of these ideas can be changed if you have something particularly different / special in mind etc.

P.S Coding is not required, just a design.

- Our website -

Our website is simply a price comparison website that allows customers to find companies within their area at the best price. The products available are mostly related to the vehicle trade and all refer to vinyl. This includes the likes of vehicle window tint, vehicle colour change vehicle wrap, vehicle signage as well as other cosmetic vinyl modifications. We allow the customer to search for their product within their chosen area and receive a list of companies who supply their product within that area. From here they can compare prices and view further details on the company.

- What we're looking to do -

We're looking first of all to adjust how the website homepage is displayed, this includes adding images and adjusting the colours that are explained below:

First of all, we look to spread out each of the 12 products (which can be seen on the website as it stands) and add an image to each of the products (all being spaced out as shown in our sketch)

We've been told the website looks too busy so we're thinking if we adjust the colours to more simplier neutral colours as well as the main focus of the website being on the 12 images, that would be great.

- Logo + Banner -

Logo to remain top left although banner may be removed / adjusted to make simplier.

- Colours -

Adjustments - Colours shades
We want the website to still look exciting but simplify the colours. Needs to be kept up to date with the colours / textures etc (bright colours to highlight keypoints)
We're still looking to use either blue or orange or maybe both to highlight these keypoints but the main website to be light colours and maybe even black on white background. The entire homepage can be adjusted colour wise if you feel it fits into your theme including menu bars, banners etc. The key is to get this right with being not too overpowering with the colours but still look interesting and up to date.

- 1 - 4 steps banner - (text may change)

This sits just under the logo and explains to the user how easy the website is to use and the steps they need to take. This may change to a 1 - 5 steps but we're looking to have this designed once the overall colours / theme of the website is sorted.

- 12 images - 4 x 3

This is the main focus of the website and will be the main focus of what the customer sees first of all. This will be where they select their product and then underneath, enter their postcode and distance they would like to search within. As explained further up, we have some of the product images available so if you can where possible add these to the design and then duplicate the images on those we currently don't have available.

- 12 Images -Titles -

These titles will be in this order from left to right and etc

- Colour Change Wrap
- Printed Vehicle Wrap
- Window Tint
- Headlight Tint
- Vehicle Signage
- Shop Signage
- Roof Vinyl Wrap
- Bonnet Vinyl Wrap
- Carbon Fibre Vinyl
- Stickerbomb Vinyl
- Clear Protective Vinyl
- Wheel Refurb

Text to be quite large, centered and with the o to the left of the title. Short titles like 'Window Tint' should fit on one line in the middle of the box where as titles such as ' Stickerbomb Vinyl Wrap' should have the 'Stickerbomb Vinyl' on the first line with the 'Wrap' on the line below. The background of this text is up to experient, might be worth just a simple colour or it might be worth using a bright blue or orange to keep in with the theme of the logo etc.

These will also have the circle tick box to the left of the title (as on the current website) where the customer clicks to select the product they have available.
We were also thinking that if when the customer ticks the circle on their selected box, the box is highlighted in some way to show this.

- Search Block -

This will appear under the 12 images and allows the customer to input their postcode and distance for the search criteria. Colours on this can of course be adjusted to keep in theme with the website.

- Under the 12 Images -

- Block underneath the 12 images and search block -

To the left will be some key bullet points about the website - maybe 4 or 5 with a green tick to the left of this. Background colour will probably be best to be a light colour, possibly grey.

Then to the right of this will appear 4 images, 2 before and 2 after when applying these products. Images to be used aren't fully decided on and we would like this stage of the design left to the end when the rest of the theme etc have been decided on.

Attached images are as follows :
- How the website looks as it stands
- The fold line on the website (obviously important)
- Our rough sketch of how we'd like the website homepage to look.
- We have 7 of the images ready that are all attached in this one file. Please duplicate the images on those that currently don't have the image available.

We will also be requesting a website developer to put this into action if our current designer falls through so please feel free to contact us if potentially interested.

The layout can change if you can think of something particular different / unique that works with this design. The main idea is to not only get the 12 products on view to the viewers but also the keypoints and before and after images.

Any questions, please ask away as we're bound to have forgotten a few things.

Thanks and good luck!

Hi all, keep the designs coming.

We haven't quite seen that extra special design we're after. As stated, we're after something fairly simple to suit the youth as well as the middle aged but we're also after something that bit special.

Colours to concentrate on are still and orange etc although feel free to use other colours if you have anything special in mind.

Please experience and we'll give you our honest feedback.

Many thanks all and good luck!

Hi all, this is a message to all the designers.

Some good designs coming in but we're still after that something special for the website design. Keep the designs coming and please feel free to experiment with the design colours, layout etc.

The basic principle of the website needs to remain regarding the 12 products, search within block and 4 steps all appearing on the homepage.

The 4 steps seems to work best when it's got text as well as some simple images next to this.

A variation with the product titles with how to display this, some designers have gone with a simple white background whereas others have gone with colours. Please experiment here and where possible, add a contract / texture to the colour. Please remember the product titles needs to be clear, centured and with the circle tick box to the left of it. 

We're after a fairly simple design although we need it to look 21st century, up to date as well as interesting. The key points straight away are the 4 steps as well as the 12 products so try to guide the viewer to these areas a little.

White background behind the 12 images seems to be a much, although a light colour could possibly work.

The keypoints underneath these 12 products are too very important as it outlines what we do etc. Tick colour can vary.

Next to these keypoints will be the 'before' and 'after' images, these images needs to be fairly small and ensure there is white background around the image itself.

Good luck all and any questions, feel free to ask away.

Thanks!

Hi,

 Thank you for your time and effort with these designs, we are very nearly there with the design but we've thought of something that may work for the homepage. A curved arrow from step 1 pointing to the products, this may or may not work but feel free to give it a go.

Many thanks,

Thank you to everyone for your time and efforts with the design. It's hugely appreciated so thank you all once again.

Wish you all the luck in the future.

```html
<!DOCTYPE html>
<html lang="en">
<head>
<meta charset="utf-8">
<title>Wrapscout – Find a Professional Vinyl Installer</title>
<link href="https://fonts.googleapis.com/css2?family=Source+Sans+3:wght@400;600;700&display=swap" rel="stylesheet">
<style>
:root{
  --navy:#2b3866;
  --orange:#f7a233;
  --orange-dark:#ef8f1f;
  --page:#ebebeb;
  --card:#ffffff;
  --line:#d9d9d9;
  --ink:#333333;
  --step1:#7d95e6;
  --step2:#6279c9;
  --step3:#4a5ea6;
  --step4:#35457e;
  --sky-top:#dfeaf5;
  --sky-bottom:#ffffff;
}
*{margin:0;padding:0;box-sizing:border-box}
html,body{width:806px;height:1200px;overflow:hidden}
body{position:relative;background:var(--page);font-family:"Source Sans 3",Arial,sans-serif;color:var(--ink)}
.abs{position:absolute}

.header{left:0;top:0;width:806px;height:144px;background:linear-gradient(180deg,var(--sky-top),var(--sky-bottom) 85%)}
.topnav{left:0;top:0;width:806px;height:32px;background:rgba(255,255,255,.55)}
.topnav a{position:absolute;top:10px;font-size:10px;color:var(--ink);text-decoration:none}
.topnav a.active{color:var(--navy)}
.social{width:17px;height:17px;border-radius:50%;background:#111}

.brand{left:82px;top:58px;display:flex;align-items:center;gap:10px}
.brand-dot{width:38px;height:38px;border-radius:50%;background:var(--orange)}
.brand-name{font-size:32px;font-weight:700;color:var(--navy);letter-spacing:.5px}
.brand-tag{left:130px;top:96px;font-size:10px;font-weight:600;color:var(--navy)}
.vans{left:462px;top:52px;width:276px;height:78px;border-radius:8px;background:linear-gradient(90deg,#e4e6e9,#d6dade 50%,#c9d3c6)}

.hero-band{left:0;top:144px;width:806px;height:37px;background:linear-gradient(180deg,var(--orange),var(--orange-dark));color:#fff;font-size:17px;font-weight:600;text-align:center;line-height:37px}

.steps{left:0;top:181px;width:806px;height:68px;background:#fff}
.step{position:absolute;display:flex;align-items:flex-start;gap:9px;font-size:10.5px;line-height:15px;color:#444;text-transform:uppercase}
.step svg{flex:none}
.step-bars{left:69px;top:249px;width:662px;height:5px;display:flex}
.step-bars span{flex:1}

.grid{left:70px;top:292px;width:662px;display:grid;grid-template-columns:repeat(4,161px);grid-auto-rows:180px;gap:6px}
.product{background:var(--card);border:1px solid var(--line);padding:3px}
.product-photo{height:134px}
.product-title{text-align:center;font-size:12.5px;line-height:40px;color:#333;text-transform:uppercase}
.product.selected{background:var(--navy);border-color:var(--navy)}
.product.selected .product-title{color:#fff}

.keypoints{left:70px;top:877px;width:205px;height:136px;background:var(--navy);padding:20px 0 0 14px}
.keypoints li{list-style:none;display:flex;align-items:center;gap:10px;color:#fff;font-size:9.5px;font-weight:600;text-transform:uppercase;height:24px}
.showcase{left:275px;top:877px;width:457px;height:136px;background:var(--page);border-bottom:4px solid var(--navy)}
.shot{position:absolute;top:5px;width:166px;height:96px;background:#fff;border:4px solid #c9c9c9;padding:8px 14px}
.shot-photo{width:100%;height:100%;border-radius:6px;background:linear-gradient(180deg,#5cbf4f,#2f8c2d)}
.shot-label{position:absolute;top:112px;width:166px;text-align:center;font-size:12.5px;color:var(--navy);text-transform:uppercase}
.mascot{left:646px;top:944px;width:92px;height:64px;border-radius:10px;background:var(--orange)}

.footer{left:0;top:1062px;width:806px;height:107px;background:var(--navy)}
.footer-notch{left:387px;top:1062px;width:0;height:0;border-left:16px solid transparent;border-right:16px solid transparent;border-top:12px solid var(--page)}
.footer a{position:absolute;top:53px;font-size:10px;font-weight:600;color:var(--orange);text-decoration:none}
.footer .social{background:var(--orange);top:47px}
.copyright{left:0;top:1169px;width:806px;height:31px;background:#fff;text-align:center;font-size:8.5px;line-height:24px;color:#222}
</style>
</head>
<body>

<header class="abs header">
  <nav class="abs topnav">
    <a class="active" style="left:103px">HOME</a>
    <a style="left:170px">ABOUT US</a>
    <a style="left:249px">CONTACT US</a>
    <a style="left:341px">BLOG</a>
    <a style="left:403px">LIST YOUR COMPANY HERE</a>
    <span class="abs social" style="left:684px;top:7px" aria-label="Social link"></span>
    <span class="abs social" style="left:709px;top:7px" aria-label="Social link"></span>
  </nav>
  <div class="abs brand"><span class="brand-dot"></span><span class="brand-name">Wrapscout</span></div>
  <div class="abs brand-tag">Compare local wrap fitters</div>
  <div class="abs vans" role="img" aria-label="Wrapped vans and a sticker-covered car"></div>
</header>

<div class="abs hero-band">Find a Professional Vinyl Installer</div>

<section class="abs steps">
  <div class="step" style="left:90px;top:25px">
    <svg width="28" height="34" viewBox="0 0 28 34"><rect x="1" y="0" width="5" height="34" rx="2" fill="var(--step1)"/><rect x="7" y="6" width="20" height="24" fill="var(--step1)"/></svg>
    <span>Select chosen<br>product</span>
  </div>
  <div class="step" style="left:246px;top:26px">
    <svg width="24" height="32" viewBox="0 0 24 32"><path d="M12 1C6 1 2 5.5 2 11c0 7 10 20 10 20s10-13 10-20C22 5.5 18 1 12 1z" fill="var(--step2)"/><circle cx="12" cy="11" r="4" fill="#fff"/></svg>
    <span>Input postcode +<br>distance + search</span>
  </div>
  <div class="step" style="left:407px;top:28px">
    <svg width="26" height="28" viewBox="0 0 26 28"><path d="M2 10L11 1l13 13-10 13L2 15z" fill="var(--step3)"/><circle cx="9" cy="9" r="2.5" fill="#fff"/></svg>
    <span>Compare companies +<br>prices</span>
  </div>
  <div class="step" style="left:590px;top:28px">
    <svg width="22" height="24" viewBox="0 0 22 24"><path d="M4 1l5 5-3 3c1 4 4 7 8 9l3-3 5 5-4 4C9 22 1 13 0 5z" fill="var(--step4)"/></svg>
    <span>Contact chosen<br>company</span>
  </div>
</section>
<div class="abs step-bars"><span style="background:var(--step1)"></span><span style="background:var(--step2)"></span><span style="background:var(--step3)"></span><span style="background:var(--step4)"></span></div>

<main class="abs grid">
  <div class="product selected"><div class="product-photo" role="img" aria-label="Fitter applying a colour change wrap to a car" style="background:linear-gradient(180deg,#5d6f78,#2f3a4c)"></div><div class="product-title">Colour Change Wrap</div></div>
  <div class="product"><div class="product-photo" role="img" aria-label="Small car with a printed wrap" style="background:linear-gradient(180deg,#a86a58,#5a48a8)"></div><div class="product-title">Printed Vehicle Wrap</div></div>
  <div class="product"><div class="product-photo" role="img" aria-label="Tinted car window" style="background:linear-gradient(180deg,#6f8f58,#1f4646)"></div><div class="product-title">Window Tint</div></div>
  <div class="product"><div class="product-photo" role="img" aria-label="Car front with tinted headlights" style="background:linear-gradient(180deg,#8c948c,#22283a)"></div><div class="product-title">Headlight Tint</div></div>

  <div class="product"><div class="product-photo" role="img" aria-label="White van with signage" style="background:linear-gradient(180deg,#f2f2f2,#d4d7db)"></div><div class="product-title">Vehicle Signage</div></div>
  <div class="product"><div class="product-photo" role="img" aria-label="Shop front with window signage" style="background:linear-gradient(180deg,#d8d8d8,#8c8c8c)"></div><div class="product-title">Shop Signage</div></div>
  <div class="product"><div class="product-photo" role="img" aria-label="Silver car with a black vinyl roof" style="background:linear-gradient(180deg,#c9cbce,#9a9da1)"></div><div class="product-title">Roof Vinyl Wrap</div></div>
  <div class="product"><div class="product-photo" role="img" aria-label="Silver car with a black vinyl bonnet" style="background:linear-gradient(180deg,#c4c6c9,#94979b)"></div><div class="product-title">Bonet Vinyl Wrap</div></div>

  <div class="product"><div class="product-photo" role="img" aria-label="Carbon fibre vinyl on a car panel" style="background:linear-gradient(180deg,#5e5e5e,#222)"></div><div class="product-title">Carbon Fiber Vinyl</div></div>
  <div class="product"><div class="product-photo" role="img" aria-label="Car covered in colourful printed vinyl" style="background:linear-gradient(180deg,#6a8cb8,#b05060)"></div><div class="product-title">Sticker&nbsp; Vinyl</div></div>
  <div class="product"><div class="product-photo" role="img" aria-label="Clear protective film being applied" style="background:linear-gradient(180deg,#8a8fb8,#2e3258)"></div><div class="product-title">Clear Protective Vinyl</div></div>
  <div class="product"><div class="product-photo" role="img" aria-label="Refurbished alloy wheel" style="background:linear-gradient(180deg,#3c4a66,#14192a)"></div><div class="product-title">Wheel Refurb</div></div>
</main>

<section class="abs keypoints">
  <ul>
    <li><svg width="14" height="10" viewBox="0 0 14 10"><path d="M1 5l4 4 8-8" fill="none" stroke="#fff" stroke-width="1.4"/></svg>Proin gravida nibh vel velit</li>
    <li><svg width="14" height="10" viewBox="0 0 14 10"><path d="M1 5l4 4 8-8" fill="none" stroke="#fff" stroke-width="1.4"/></svg>Auctorquetaenean</li>
    <li><svg width="14" height="10" viewBox="0 0 14 10"><path d="M1 5l4 4 8-8" fill="none" stroke="#fff" stroke-width="1.4"/></svg>Sollicitudin,lorqbibendum</li>
    <li><svg width="14" height="10" viewBox="0 0 14 10"><path d="M1 5l4 4 8-8" fill="none" stroke="#fff" stroke-width="1.4"/></svg>Auctor elit consqipsum nec sagi</li>
  </ul>
</section>

<section class="abs showcase">
  <svg class="abs" style="left:16px;top:38px" width="10" height="18" viewBox="0 0 10 18"><path d="M9 1L1 9l8 8" fill="none" stroke="var(--navy)" stroke-width="1.4"/></svg>
  <div class="shot" style="left:45px"><div class="shot-photo" role="img" aria-label="Green hatchback before vinyl work"></div></div>
  <div class="shot-label" style="left:45px">Before</div>
  <div class="shot" style="left:225px"><div class="shot-photo" role="img" aria-label="Green hatchback after vinyl work"></div></div>
  <div class="shot-label" style="left:225px">After</div>
  <svg class="abs" style="left:413px;top:38px" width="10" height="18" viewBox="0 0 10 18"><path d="M1 1l8 8-8 8" fill="none" stroke="var(--navy)" stroke-width="1.4"/></svg>
</section>
<div class="abs mascot" role="img" aria-label="Orange brand mascot character"></div>

<footer class="abs footer">
  <a style="left:88px">HOME</a>
  <a style="left:154px">ABOUT US</a>
  <a style="left:234px">CONTACT US</a>
  <a style="left:325px">BLOG</a>
  <a style="left:388px">LIST YOUR COMPANY HERE</a>
  <span class="abs social" style="left:672px" aria-label="Social link"></span>
  <span class="abs social" style="left:698px" aria-label="Social link"></span>
</footer>
<div class="abs footer-notch"></div>
<div class="abs copyright">© Copyright 2013 Wrapscout</div>

</body>
</html>
```